Business Card Design for an Investment Company

We need a business card design for our private investment company, called Dunmore Equity. Dunmore Equity is an investments partnership that aims to acquire shares in listed companies with a view to influencing those companies through active dialogue in order to improve their value. We need designs that use the logo colors (blue, grey, white), we need both English and Arabic on the business cards (can be on one side or 2 sides). The final logo should communicate professionalism, conservatism (nothing too fancy or too cheesy), that we are smart, conservative and old school.

Target Market(s)

Investment companies

Industry/Entity Type

Investment

Contact Information for Business Card

Tariq Salmanuddin Farouqi
Senior Executive Officer

Harbor Court 07, Level 3, Office 214/12
QTFZ

+9714987650
tfarouqi@dunmore-equity.com
www.dunmore-equity.com

Requirements
Must have
• Logo to be placed on the left hand side of the business card
• for the Arabic, we only need to have the name and title so it can be accomodated on one side so we can have the other side with full color and logo. The arabic that needs to be used is the below:
• طارق سلمان الدين فاروقي
• المدير التنفيدي

```html
<!DOCTYPE html>
<html lang="en">
<head>
<meta charset="utf-8">
<title>Dunmore Equity — Business Card</title>
<link rel="stylesheet" href="https://fonts.googleapis.com/css2?family=Roboto:wght@400;700&family=Lato:wght@400;700&family=Noto+Kufi+Arabic:wght@400;700&display=swap">
<style>
  :root {
    --stage: #ececec;
    --card-dark: #5a5a5c;
    --card-dark-deep: #4a4a4c;
    --card-light: #ffffff;
    --ink: #1f1f1f;
    --grey: #555557;
    --blue: #0b5aa8;
    --blue-text: #1c5c9f;
    --white: #ffffff;
  }
  * { margin: 0; padding: 0; box-sizing: border-box; }
  html, body { width: 1200px; height: 586px; overflow: hidden; }
  body {
    background: var(--stage);
    position: relative;
    font-family: "Lato", Arial, sans-serif;
  }
  .card {
    position: absolute;
    top: 129px;
    width: 501px;
    height: 300px;
    overflow: hidden;
  }
  .card--front { left: 61px; background: var(--card-dark); }
  .card--back { left: 619px; background: var(--card-light); }

  .front-texture {
    position: absolute; inset: 0;
    background: linear-gradient(135deg, #606062 0%, var(--card-dark) 50%, var(--card-dark-deep) 100%);
  }
  .wordmark {
    position: absolute;
    left: 0; right: 0;
    display: flex; align-items: center; justify-content: center; gap: 12px;
    font-family: "Roboto", Arial, sans-serif;
    font-weight: 700;
    letter-spacing: -1px;
    white-space: nowrap;
  }
  .wordmark__square { display: block; flex: none; }
  .card--front .wordmark { top: 124px; font-size: 50px; color: var(--white); }
  .card--front .wordmark__square { width: 16px; height: 16px; background: var(--white); }
  .card--back .wordmark { top: 46px; font-size: 44px; color: var(--blue-text); }
  .card--back .wordmark__square { width: 14px; height: 14px; background: var(--grey); }

  .website {
    position: absolute; left: 0; right: 0; top: 245px;
    text-align: center;
    font-family: "Roboto", Arial, sans-serif;
    font-size: 12px;
    letter-spacing: 5px;
    color: var(--white);
  }

  .person {
    position: absolute;
    right: 263px;
    top: 158px;
    text-align: right;
  }
  .person__name { font-size: 14.5px; font-weight: 700; color: var(--blue-text); white-space: nowrap; }
  .person__title { font-size: 11px; color: var(--ink); margin-top: 3px; white-space: nowrap; }
  .person__name--ar, .person__title--ar {
    font-family: "Noto Kufi Arabic", "Lato", sans-serif;
    direction: rtl;
  }
  .person__name--ar { font-size: 13px; margin-top: 10px; }
  .person__title--ar { font-size: 10.5px; margin-top: 1px; }

  .divider {
    position: absolute; left: 250px; top: 148px;
    width: 3px; height: 112px; background: var(--grey);
  }
  .contacts {
    position: absolute; left: 266px; top: 154px;
    list-style: none;
  }
  .contacts li {
    display: flex; align-items: center; gap: 7px;
    min-height: 24px;
    font-size: 12px; color: var(--ink);
    white-space: nowrap;
  }
  .contacts li.contacts__address { font-size: 11px; line-height: 1.3; margin-top: 3px; }
  .contacts svg { width: 17px; height: 17px; flex: none; }

  .band-grey { position: absolute; left: 0; right: 0; top: 288px; height: 5px; background: var(--grey); }
  .band-blue { position: absolute; left: 0; right: 0; top: 293px; height: 7px; background: var(--blue); }
</style>
</head>
<body>

<section class="card card--front">
  <div class="front-texture" role="img" aria-label="Faceted grey low-poly background texture"></div>
  <div class="wordmark"><span class="wordmark__square"></span>Dunmore Equity</div>
  <p class="website">www.dunmore-equity.com</p>
</section>

<section class="card card--back">
  <div class="wordmark"><span class="wordmark__square"></span>Dunmore Equity</div>

  <div class="person">
    <p class="person__name">Tariq Salmanuddin Farouqi</p>
    <p class="person__title">Senior Executive Officer</p>
    <p class="person__name person__name--ar" lang="ar">طارق سلمان الدين فاروقي</p>
    <p class="person__title person__title--ar" lang="ar">المدير التنفيدي</p>
  </div>

  <div class="divider"></div>

  <ul class="contacts">
    <li>
      <svg viewBox="0 0 20 20" aria-hidden="true">
        <circle cx="10" cy="10" r="10" fill="var(--blue)"/>
        <path d="M5 8.5c0-1.5 2.2-2.5 5-2.5s5 1 5 2.5v.8h-2.4V8.3H7.4v1H5z" fill="#fff"/>
        <rect x="6" y="10" width="8" height="4.5" rx="1" fill="#fff"/>
      </svg>
      +9714987650
    </li>
    <li>
      <svg viewBox="0 0 20 20" aria-hidden="true">
        <circle cx="10" cy="10" r="10" fill="var(--blue)"/>
        <rect x="7" y="5" width="6" height="3" fill="#fff"/>
        <rect x="5" y="8.5" width="10" height="4.5" rx="1" fill="#fff"/>
        <rect x="7" y="11.5" width="6" height="3.5" fill="#fff" stroke="var(--blue)" stroke-width="0.8"/>
      </svg>
      +9714987651
    </li>
    <li>
      <svg viewBox="0 0 20 20" aria-hidden="true">
        <circle cx="10" cy="10" r="10" fill="var(--blue)"/>
        <rect x="5" y="6.5" width="10" height="7" fill="#fff"/>
        <path d="M5 6.5l5 4 5-4" fill="none" stroke="var(--blue)" stroke-width="1"/>
      </svg>
      tfarouqi@dunmore-equity.com
    </li>
    <li class="contacts__address">
      <svg viewBox="0 0 20 20" aria-hidden="true">
        <circle cx="10" cy="10" r="10" fill="var(--blue)"/>
        <path d="M10 4.5a3.6 3.6 0 0 0-3.6 3.6c0 2.7 3.6 7 3.6 7s3.6-4.3 3.6-7A3.6 3.6 0 0 0 10 4.5z" fill="#fff"/>
        <circle cx="10" cy="8.1" r="1.3" fill="var(--blue)"/>
      </svg>
      <span>Harbor Court 07, Level 3,<br>Office 214/12, QTFZ</span>
    </li>
  </ul>

  <div class="band-grey"></div>
  <div class="band-blue"></div>
</section>

</body>
</html>
```